Plate Bright Class (workshop to teach people to eat fruits and vegetables)

Double sided DL Flyer

Free Community Workshop
Plate Bright Live Light
Harbourview NSW

Copy to appear on flyer side one:-
PLATE BRIGHT LIVE LIGHT
interactive workshops
March-April 2019
Presented by qualified nutritionist

Food for healthier happier life for you and your family (free to Harbourview residents - all ages welcome

Side 2
Learn About:-
Foods that improve your health
basic nutrition
gut brain connection
portion size
menu planning
preparation
eating

Benefits
Improved health
Improved Energy
Manage chronic illness
diabetes type II
cholesterol
Blood Pressure
Family fun

Food Tastings
Lucky Door Prize

Reserve for spot online @ www.platebright.com.au or call 0482 916 304
Supported by Harbourview Shire Council (Logo) Tidewater Rovers Club (Logo) Pinebrook Veterans Club (Logo)

I would like to see a flyer that is bright, fun and fresh with images of fresh food.

Target Market(s)

Women 30 plus

Industry/Entity Type

Health And Wellness

Logo Text

PLATE BRIGHT LIVE LIGHT

Font styles to use
Other font styles liked:
• bold clean

Colors
f37122
9bcb3c
fbed22
ec1f27
e34297

Requirements
Must have
• bright eye catching colours featuring fresh fruit and vegetables
• I have attached a some images of designs I like
Nice to have
• Im happy for the designer to change copy to create a clean flyer without loosing essential information
• I like the feel of the banner on my facebook page
• Sunroot Kitchen - Plate Bright Live Light with Delia Frome
• https://www.facebook.com/sunrootkitchenoz/
Should not have
• old fashioned images

```html
<!DOCTYPE html>
<html lang="en">
<head>
<meta charset="utf-8">
<title>Plate Bright Live Light – DL Flyer</title>
<link href="https://fonts.googleapis.com/css2?family=Montserrat:ital,wght@0,500;0,600;0,700;0,800;0,900;1,500&display=swap" rel="stylesheet">
<style>
  :root {
    --orange: #f37122;
    --green: #9bcb3c;
    --yellow: #fbed22;
    --red: #ec1f27;
    --pink: #e34297;
    --blue: #1f9ad6;
    --sky: #7fd0f2;
    --sky-pale: #e3f5fd;
    --navy: #1e3f73;
    --ink: #2b2b2b;
    --stage: #e4e4e4;
    --white: #ffffff;
  }
  * { box-sizing: border-box; margin: 0; padding: 0; }
  html, body { width: 800px; height: 1200px; overflow: hidden; }
  body {
    background: var(--stage);
    font-family: "Montserrat", Arial, sans-serif;
    color: var(--ink);
    position: relative;
  }
  .flyer-side {
    position: absolute;
    left: 40px;
    width: 720px;
    height: 340px;
    background: var(--white);
    overflow: hidden;
    box-shadow: 0 6px 18px rgba(0,0,0,.18);
  }
  .side-front { top: 230px; background: linear-gradient(180deg, var(--sky-pale) 0%, var(--white) 45%, var(--white) 80%, var(--sky-pale) 100%); }
  .side-back { top: 630px; }

  /* front */
  .headline {
    position: absolute; left: 26px; top: 24px; width: 350px;
    font-weight: 900; font-size: 40px; line-height: 1; letter-spacing: -1px;
    white-space: nowrap;
  }
  .headline .line-one { color: var(--pink); display: block; }
  .headline .line-two { color: var(--sky); display: block; }
  .dates-banner {
    position: absolute; left: 400px; top: 22px;
    background: var(--blue); color: var(--white);
    padding: 8px 18px 10px; border-radius: 0 0 0 22px;
    width: 290px;
  }
  .dates-banner .kicker { font-size: 15px; font-weight: 600; display: block; }
  .dates-banner .dates { font-size: 22px; font-weight: 800; display: block; }
  .produce-photo {
    position: absolute; left: 430px; top: 100px; width: 270px; height: 170px;
    border-radius: 50% 50% 40% 40% / 55% 55% 45% 45%;
    background: radial-gradient(circle at 35% 55%, #f39a3a 0%, #e67a1e 30%, #9bcb3c 60%, #c89a5e 85%);
  }
  .presenter-band {
    position: absolute; left: 0; top: 148px; width: 410px;
    background: var(--pink); color: var(--white);
    font-size: 15px; font-weight: 700; padding: 6px 26px;
  }
  .highlights { position: absolute; left: 26px; top: 190px; list-style: none; }
  .highlights li {
    display: inline-block; font-size: 12.5px; font-weight: 700;
    padding: 4px 10px; margin-bottom: 5px; color: var(--ink);
  }
  .highlights .hl-green { background: var(--green); }
  .highlights .hl-yellow { background: var(--yellow); }
  .highlights .hl-orange { background: var(--orange); color: var(--white); }
  .intro-note {
    position: absolute; left: 26px; top: 290px; width: 380px;
    font-size: 9.5px; font-style: italic; font-weight: 500; color: var(--blue);
  }
  .front-web {
    position: absolute; right: 26px; bottom: 14px;
    font-size: 13px; font-weight: 700; color: var(--navy);
  }

  /* back */
  .back-top { position: absolute; left: 0; top: 0; width: 720px; height: 262px; background: linear-gradient(180deg, var(--sky-pale), var(--white)); }
  .topic-column { position: absolute; top: 22px; }
  .topic-learn { left: 26px; width: 200px; }
  .topic-benefits { left: 230px; width: 200px; }
  .topic-tag { display: inline-block; font-size: 13px; font-weight: 800; padding: 3px 12px; margin-bottom: 8px; }
  .topic-learn .topic-tag { background: var(--yellow); }
  .topic-benefits .topic-tag { background: var(--green); color: var(--white); }
  .topic-list { list-style: none; font-size: 11px; font-weight: 600; line-height: 1.45; }
  .topic-list li::before { content: "• "; color: var(--pink); }
  .topic-list .sub { padding-left: 12px; font-weight: 500; }
  .topic-list .sub::before { content: "– "; color: var(--blue); }
  .person-photo {
    position: absolute; left: 440px; top: 0; width: 280px; height: 262px;
    background: linear-gradient(120deg, #f4ede6 0%, #d9b59a 45%, #9bcb3c 80%, #f0f7e4 100%);
  }
  .tasting-badge {
    position: absolute; left: 170px; top: 190px;
    background: var(--pink); color: var(--yellow);
    padding: 6px 22px 8px; text-align: center;
    clip-path: polygon(4% 0, 100% 0, 96% 100%, 0 100%);
  }
  .tasting-badge .small { display: block; font-size: 14px; font-weight: 700; color: var(--white); }
  .tasting-badge .big { display: block; font-size: 22px; font-weight: 900; }
  .back-footer {
    position: absolute; left: 0; bottom: 0; width: 720px; height: 78px;
    background: var(--white); border-top: 4px solid var(--sky);
  }
  .reserve {
    position: absolute; left: 26px; top: 20px; width: 370px;
    font-size: 12px; font-weight: 700; color: var(--navy); line-height: 1.45;
    white-space: nowrap;
  }
  .supporters { position: absolute; left: 410px; top: 14px; width: 290px; }
  .supporters .label { font-size: 10px; font-weight: 700; color: var(--ink); display: block; margin-bottom: 6px; }
  .supporter-row { display: flex; gap: 12px; align-items: center; }
  .supporter { display: flex; align-items: center; gap: 4px; font-size: 9px; font-weight: 700; color: var(--navy); line-height: 1.1; }
  .supporter .dot { width: 14px; height: 14px; border-radius: 50%; background: var(--blue); flex: none; }
</style>
</head>
<body>

<section class="flyer-side side-front">
  <h1 class="headline"><span class="line-one">PLATE BRIGHT</span><span class="line-two">LIVE LIGHT</span></h1>
  <div class="dates-banner"><span class="kicker">Interactive workshops</span><span class="dates">March-April 2019</span></div>
  <div class="produce-photo" role="img" aria-label="Basket of fresh fruit: oranges, apples and grapes"></div>
  <div class="presenter-band">Presented by qualified nutritionist</div>
  <ul class="highlights">
    <li class="hl-green">Food for healthier happier life for you and your family</li><br>
    <li class="hl-yellow">Free to Harbourview residents</li><br>
    <li class="hl-orange">All ages welcome</li>
  </ul>
  <p class="intro-note">Join us to discover how fresh fruit and vegetables can shape a healthier everyday life.</p>
  <p class="front-web">www.platebright.com.au</p>
</section>

<section class="flyer-side side-back">
  <div class="back-top"></div>
  <div class="topic-column topic-learn">
    <span class="topic-tag">Learn About:</span>
    <ul class="topic-list">
      <li>Foods that improve your health</li>
      <li>basic nutrition</li>
      <li>gut brain connection</li>
      <li>portion size</li>
      <li>menu planning</li>
      <li>preparation</li>
      <li>eating</li>
    </ul>
  </div>
  <div class="topic-column topic-benefits">
    <span class="topic-tag">Benefits:</span>
    <ul class="topic-list">
      <li>Improved health</li>
      <li>Improved Energy</li>
      <li>Manage Chronic Illness</li>
      <li class="sub">Diabetes Type II</li>
      <li class="sub">Cholesterol</li>
      <li class="sub">Blood Pressure</li>
      <li>Family fun</li>
    </ul>
  </div>
  <div class="person-photo" role="img" aria-label="Smiling woman eating a fresh salad"></div>
  <div class="tasting-badge"><span class="small">Food Tastings</span><span class="big">Lucky Door Prize</span></div>
  <footer class="back-footer">
    <p class="reserve">Reserve for spot online @ www.platebright.com.au<br>or call 0482 916 304</p>
    <div class="supporters">
      <span class="label">Supported by</span>
      <div class="supporter-row">
        <span class="supporter"><span class="dot"></span>Harbourview<br>Shire Council</span>
        <span class="supporter"><span class="dot"></span>Tidewater<br>Rovers Club</span>
        <span class="supporter"><span class="dot"></span>Pinebrook<br>Veterans Club</span>
      </div>
    </div>
  </footer>
</section>

</body>
</html>
```